The Harlow Law Firm, PC

Dwight K. Harlow
Attorney at Law
physical address: 728 E. 9th Avenue
Greenville, NC 27561

mailing: P.O. Box 5873
Greenville, NC 27563

o. 252.431.6672
f. 252.431.8815

www.harlowlegal-example.com

Industry/Entity Type

Attorney

Contact Information for Business Card

Attorney name
Office Phone number
Office Fax number
Mailing address and physical address
website address

Requirements
Must have
• Clean fresh design - I hate the website

```html
<!DOCTYPE html>
<html lang="en">
<head>
<meta charset="utf-8">
<title>The Harlow Law Firm, PC — Business Card</title>
<link rel="stylesheet" href="https://fonts.googleapis.com/css2?family=Arimo:wght@400;700&display=swap">
<style>
  :root {
    --page: #f4f2ef;
    --card-brown: #5a4942;
    --band-cream: #e9dabd;
    --panel-light: #f7efdf;
    --panel-warm: #d9c29c;
    --ink-dark: #4a3a32;
    --text-light: #ffffff;
    --accent-tan: #d8b98a;
  }
  html, body {
    margin: 0;
    width: 1200px;
    height: 1041px;
    overflow: hidden;
    background: var(--page);
    font-family: "Arimo", Arial, sans-serif;
  }
  .business-card {
    position: absolute;
    left: 100px;
    top: 235px;
    width: 1000px;
    height: 572px;
    background: var(--card-brown);
    overflow: hidden;
    box-shadow: 0 6px 24px rgba(0,0,0,0.18);
  }
  .cream-band {
    position: absolute;
    left: 0;
    top: 34px;
    width: 100%;
    height: 118px;
    background: var(--band-cream);
  }
  .firm-panel {
    position: absolute;
    left: 272px;
    top: 0;
    width: 580px;
    height: 252px;
    background: radial-gradient(ellipse at 50% 45%, var(--panel-light) 0%, #eddcbc 55%, var(--panel-warm) 100%);
    display: flex;
    align-items: center;
    justify-content: center;
  }
  .firm-name {
    margin: 0;
    color: var(--ink-dark);
    font-weight: 400;
    font-size: 54px;
    line-height: 1.08;
    letter-spacing: 1px;
    text-align: center;
  }
  .attorney {
    position: absolute;
    left: 48px;
    top: 350px;
    color: var(--text-light);
  }
  .attorney-name {
    margin: 0;
    font-weight: 700;
    font-size: 42px;
    line-height: 1.1;
  }
  .attorney-title {
    margin: 4px 0 0;
    font-size: 20px;
    letter-spacing: 1px;
    text-transform: uppercase;
  }
  .phones {
    position: absolute;
    left: 48px;
    top: 445px;
    color: var(--text-light);
    font-size: 22px;
    line-height: 1.4;
  }
  .phones p, .address p { margin: 0; }
  .label { color: var(--accent-tan); font-size: 19px; }
  .website {
    position: absolute;
    left: 48px;
    top: 520px;
    margin: 0;
    color: var(--text-light);
    font-size: 22px;
  }
  .address {
    position: absolute;
    right: 48px;
    color: var(--text-light);
    font-size: 22px;
    line-height: 1.4;
    text-align: right;
  }
  .address-physical { top: 375px; }
  .address-mailing { top: 468px; }
</style>
</head>
<body>
  <section class="business-card">
    <div class="cream-band"></div>
    <div class="firm-panel">
      <h1 class="firm-name">The Harlow<br>Law Firm, PC</h1>
    </div>

    <div class="attorney">
      <h2 class="attorney-name">Dwight K. Harlow</h2>
      <p class="attorney-title">Attorney at Law</p>
    </div>

    <div class="phones">
      <p>252.431.6672 <span class="label">(office)</span></p>
      <p>252.431.8815 <span class="label">(facsimile)</span></p>
    </div>

    <p class="website">www.harlowlegal-example.com</p>

    <div class="address address-physical">
      <p>728 E. 9th Avenue</p>
      <p>Greenville, NC 27561</p>
    </div>

    <div class="address address-mailing">
      <p><span class="label">(mailing)</span> P.O. Box 5873</p>
      <p>Greenville, NC 27563</p>
    </div>
  </section>
</body>
</html>
```